Real EState

A real estate company. I want to start a mailing of 1,000 standard size post cards. I want to mail these every month. Starting Jan 2015. The first 1,000 talking about this new year, the following months something to do with the seasons or holidays upcoming. I would like the design to be familiar each month so that my company will be recognized. I can send you my business card and logo which has my address phone# etc. I only want to spend the $29 design change each month, not the $180. I believe this should be attainable knowing I want consistency, I want my clients to easily know who my company is and I am available to help them get their real estate needs accomplished. One phrase I would like them to read each time is this. Why don't you take this opportunity now and give me a call or stop by because " When you open our door, it will definitely open doors for you.

I am not good at this type communication. I would really like to speak to someone. I know we cannot so please bare with me. I have no idea if my brief has gone out to everyone or not. here is what I would like. My logo needs to be there. The letters K&R PROPERTIES needs to be in gold. The buildings and lines going across need to be a light gray. I would like to see a nice quality door along with maybe a side light window. There needs to be a key in the door. I would like to see the door opening. I also want the phrase that I sent to everyone regarding opening the door. All other colors need to blend in with the colors of the logo. Lets put in all the phone numbers on the business card along with the e-mail address. Please at this time leave off the web address until I can update the site.

Reason: I am not good at this kind of communication. My computer skills are not good enough to even understand the programs your using. I don't even know if everyone is getting my explanations or even the feed back. Every time I try to bring up a design I lose the page in front of me I think I am getting better working your system but time will tell. Please bare with me. I will be loyal to the designer that can give what I need but again I'm having a hard time knowing who's who and keeping track of them.

Industry/Entity Type

Real Estate

```html
<!DOCTYPE html>
<html lang="en">
<head>
<meta charset="utf-8">
<title>K&amp;R Properties Postcard</title>
<link rel="stylesheet" href="https://fonts.googleapis.com/css2?family=League+Gothic&family=Roboto+Slab:wght@300&family=Arimo:wght@400;700&display=swap">
<style>
  :root {
    --ink: #4a4a4a;
    --red: #e2343c;
    --dark: #3b2f2c;
    --orange: #c0602d;
    --gold: #d4a23f;
    --grey: #555555;
    --rule: #8a8a8a;
    --paper: #ffffff;
  }
  * { margin: 0; padding: 0; box-sizing: border-box; }
  html, body { width: 883px; height: 1200px; overflow: hidden; background: var(--paper); }
  body { position: relative; font-family: "Arimo", Arial, sans-serif; }

  .card-front { position: absolute; left: 0; top: 0; width: 883px; height: 588px; border: 1px solid #bbb; overflow: hidden; background: var(--paper); }
  .door-photo { position: absolute; left: 0; top: 0; width: 215px; height: 588px;
    background: linear-gradient(90deg, #8a3c1c 0%, #a4532a 55%, #c9c2bc 80%, #f4f2f0 100%); }
  .front-shapes { position: absolute; left: 0; top: 0; }

  .headline { position: absolute; left: 221px; font-family: "League Gothic", "Arial Narrow", sans-serif; font-weight: 400; line-height: 1.22; white-space: nowrap; }
  .headline--invite { top: 126px; font-size: 40px; color: var(--ink); }
  .headline--promise { top: 260px; font-size: 38px; color: var(--red); letter-spacing: -0.2px; }
  .benefits { position: absolute; left: 221px; top: 377px; list-style: none; font-family: "Roboto Slab", serif; font-weight: 300; font-size: 20px; color: #333; }
  .benefits li { height: 36px; }

  .agent-photo { position: absolute; left: 721px; top: 203px; width: 115px; height: 146px; background: linear-gradient(180deg, #d9dde2, #8a8f98); }
  .agent-name { position: absolute; right: 45px; top: 378px; text-align: right; color: #fff; }
  .agent-name strong { display: block; font-size: 21px; font-weight: 700; }
  .agent-name span { display: block; font-size: 14px; font-style: italic; }
  .brand-name { position: absolute; left: 575px; top: 494px; width: 280px; text-align: center; font-size: 26px; font-weight: 700; color: var(--gold); letter-spacing: 1px; white-space: nowrap; }

  .card-back { position: absolute; left: 0; top: 610px; width: 883px; height: 590px; border: 1px solid #555; background: var(--paper); }
  .divider { position: absolute; left: 441px; top: 57px; width: 1px; height: 456px; background: var(--rule); }
  .address-line { position: absolute; left: 486px; width: 341px; height: 1px; background: var(--rule); }
  .contacts { position: absolute; left: 50px; top: 232px; list-style: none; }
  .contact { position: relative; height: 47px; padding-left: 42px; font-size: 20px; font-weight: 700; color: var(--grey); line-height: 36px; white-space: nowrap; }
  .contact svg { position: absolute; left: 0; top: 0; }
  .contact--address { line-height: 26px; padding-left: 48px; padding-top: 4px; }
</style>
</head>
<body>
  <section class="card-front">
    <div class="door-photo" role="img" aria-label="Photo of an opening wooden door with a steel handle and a key in the lock"></div>
    <svg class="front-shapes" width="883" height="588" viewBox="0 0 883 588">
      <path fill="var(--orange)" d="M590,0 C648,110 642,280 572,360 C502,430 452,500 540,588 L883,588 L883,0 Z"/>
      <path fill="none" stroke="#fff" stroke-width="2" d="M598,0 C656,110 651,280 581,360 C511,430 462,500 550,588"/>
      <path fill="var(--dark)" d="M606,0 C665,110 660,280 590,360 C520,430 472,500 560,588 L883,588 L883,0 Z"/>
      <rect x="868" y="0" width="12" height="588" fill="var(--orange)"/>
    </svg>

    <p class="headline headline--invite">Why don't you take this<br>opportunity now .</p>
    <p class="headline headline--promise">When you open our door,<br>it will definitely open doors for you.</p>
    <ul class="benefits">
      <li>Right property</li>
      <li>Right location</li>
      <li>Right Deal</li>
      <li>Right Now,</li>
      <li>More then the best.</li>
    </ul>

    <div class="agent-photo" role="img" aria-label="Portrait photo of the broker"></div>
    <p class="agent-name"><strong>Calvin J Hartley Jr.</strong><span>Broker &amp; Consultant</span></p>
    <p class="brand-name">K&amp;R PROPERTIES</p>
  </section>

  <section class="card-back">
    <div class="divider"></div>
    <div class="address-line" style="top:247px"></div>
    <div class="address-line" style="top:307px"></div>
    <div class="address-line" style="top:368px"></div>
    <div class="address-line" style="top:428px"></div>

    <ul class="contacts">
      <li class="contact">
        <svg width="36" height="36" viewBox="0 0 36 36"><circle cx="18" cy="18" r="18" fill="var(--red)"/><rect x="13" y="8" width="10" height="20" rx="2" fill="none" stroke="#fff" stroke-width="2"/><rect x="15" y="11" width="6" height="5" fill="#fff"/></svg>
        555 201 3517
      </li>
      <li class="contact">
        <svg width="36" height="36" viewBox="0 0 36 36"><circle cx="18" cy="18" r="18" fill="var(--red)"/><path d="M8,16 C12,9 24,9 28,16 L25,19 L22,16 L14,16 L11,19 Z" fill="none" stroke="#fff" stroke-width="2"/><circle cx="18" cy="22" r="3" fill="#fff"/></svg>
        555 204 4514
      </li>
      <li class="contact">
        <svg width="36" height="36" viewBox="0 0 36 36"><circle cx="18" cy="18" r="18" fill="var(--red)"/><rect x="12" y="9" width="12" height="18" fill="#fff"/><path d="M14,14 H22 M14,18 H22 M14,22 H20" stroke="var(--red)" stroke-width="1.5"/></svg>
        555 207 4518
      </li>
      <li class="contact">
        <svg width="36" height="36" viewBox="0 0 36 36"><circle cx="18" cy="18" r="18" fill="var(--red)"/><rect x="9" y="12" width="18" height="12" fill="none" stroke="#fff" stroke-width="2"/><path d="M9,12 L18,19 L27,12" fill="none" stroke="#fff" stroke-width="2"/></svg>
        calvin@krpropertiesgroup.com
      </li>
      <li class="contact">
        <svg width="36" height="36" viewBox="0 0 36 36"><circle cx="18" cy="18" r="18" fill="var(--red)"/><circle cx="18" cy="18" r="10" fill="none" stroke="#fff" stroke-width="1.6"/><ellipse cx="18" cy="18" rx="4.5" ry="10" fill="none" stroke="#fff" stroke-width="1.4"/><path d="M8,18 H28 M10,13 H26 M10,23 H26" stroke="#fff" stroke-width="1.2"/></svg>
        www.krpropertiesgroup.com
      </li>
      <li class="contact contact--address">
        <svg width="36" height="36" viewBox="0 0 36 36"><circle cx="18" cy="18" r="18" fill="var(--red)"/><path d="M18,29 C13,22 11,19 11,15 A7,7 0 0 1 25,15 C25,19 23,22 18,29 Z" fill="#fff"/><circle cx="18" cy="15" r="2.8" fill="var(--red)"/></svg>
        417, N, Birch Hollow Rd.<br>Westfield, MI 48210
      </li>
    </ul>
  </section>
</body>
</html>
```